依頼詳細
プロが業務用の高圧洗浄機を使い、ご自宅の外構・駐車場(ガレージ)・ブロック塀・玄関タイル・を綺麗にされたい方を募集します。
泥、排気ガスの汚れ、コケ、ほこり等を綺麗に致します。
お見積りは無料
高圧洗浄専門店
割引制度有
平日割引あり(火曜日・水曜日は特別料金にて実施)(空き状況はお電話にてご確認下さい)
施工料金等、丁寧に分かりやすくご説明します。
作業時間平均:2時間~3時間
料金:33,000円~
作業時:水道をお借りします
まずは、お気軽にご相談下さい。
株式会社ミドリノハウジング
TEL:094ー318-5562
担当:坂巻(さかまき)・梅沢(うめざわ)
営業時間:9:00~19:00

記載項目
株式会社ミドリノハウジング
094-318-5562
料金:33,000円~(範囲によって異なります)
プロの高圧洗浄はミドリノハウジングにお任せください。
サイズ
A4
ページ数
片面
希望イメージ
シンプル 複雑
単色 カラフル
暗い 明るい
日常 高級
遊び心 厳粛
未来的 伝統的
女性的 男性的
希望する色
水色系、ターコイズブルーの使用をお願い致します。
納品ファイル
• 高解像度JPG (.jpg)
補足説明
会社ロゴを添付しておりますので、ロゴの使用をお願い致します。
■ 選んだ理由

見やすく、弊社希望のチラシに近いものでした。
頂きました案件全てのチラシ案を印刷し、三つ折りにしましたが、一番良かったです。
伝えたい内容も、しっかり入っており、戸建てとなると年配の方が多いと思われ、その点でも大事な部分は文字が大きく見やすさも良く選ばせて頂きました。

■ 提案者全員のお礼・コメント

初めての依頼となりましたが、多数の応募を頂きましてありがとうございました。
正直、こんなに多数の応募を頂けるとは思ってませんでしたので驚きました。
今後もチラシの案をご依頼する事もるかと思いますので、宜しくお願い致します。

```html
<!DOCTYPE html>
<html lang="ja">
<head>
<meta charset="utf-8">
<title>外構洗浄 チラシ</title>
<link rel="stylesheet" href="https://fonts.googleapis.com/css2?family=M+PLUS+Rounded+1c:wght@500;700;800;900&family=Noto+Sans+JP:wght@400;500;700;900&display=swap">
<style>
:root{
  --sky:#d4f0fc;
  --sky-deep:#9edaf5;
  --blue:#0b86d6;
  --blue-dark:#0a5fb0;
  --navy:#13306e;
  --turquoise:#1fb5c9;
  --yellow:#fff04a;
  --white:#ffffff;
  --ink:#1d2a44;
}
*{margin:0;padding:0;box-sizing:border-box}
html,body{width:846px;height:1200px;overflow:hidden;background:#fff}
body{font-family:"Noto Sans JP",sans-serif;color:var(--ink)}
.flyer{position:relative;width:846px;height:1200px;overflow:hidden;background:var(--white)}
.hero-bg{position:absolute;left:0;top:0;width:846px;height:400px;background:radial-gradient(ellipse at 50% 30%,#ffffff 0%,var(--sky) 55%,var(--sky-deep) 100%)}
.rays{position:absolute;left:0;top:0}

.tagline{position:absolute;left:100px;top:28px;width:560px;height:62px;background:var(--white);border-radius:31px;box-shadow:0 3px 0 var(--sky-deep);display:flex;align-items:center;justify-content:center;font-family:"M PLUS Rounded 1c",sans-serif;font-weight:900;font-size:36px;color:var(--navy);transform:rotate(-2deg);white-space:nowrap}
.tagline em{font-style:normal;color:var(--blue)}

.weekday-badge{position:absolute;right:12px;top:12px;width:140px;height:168px;background:var(--white);border:3px solid var(--blue);border-radius:8px;text-align:center;overflow:hidden}
.weekday-badge .badge-title{background:var(--blue);color:var(--white);font-family:"M PLUS Rounded 1c",sans-serif;font-weight:900;font-size:28px;padding:6px 0;white-space:nowrap}
.weekday-badge p{font-size:13px;line-height:1.5;color:var(--navy);font-weight:700;padding:8px 4px 0;white-space:nowrap}
.weekday-badge small{display:block;font-size:11px;line-height:1.45;color:#4a5a70;font-weight:500;padding:6px 4px 0;white-space:nowrap}

.main-title{position:absolute;left:0;top:108px;width:820px;text-align:center;font-family:"M PLUS Rounded 1c",sans-serif;font-weight:900;font-size:136px;line-height:1.1;letter-spacing:6px;color:var(--blue);-webkit-text-stroke:4px var(--white);paint-order:stroke fill;text-shadow:0 6px 0 var(--navy);white-space:nowrap}

.lead{position:absolute;left:30px;top:268px;width:786px;font-family:"M PLUS Rounded 1c",sans-serif;font-weight:800;font-size:27px;line-height:1.45;color:var(--blue-dark);text-shadow:0 0 4px #fff,0 0 4px #fff;z-index:2}

.house-photo{position:absolute;left:0;top:352px;width:846px;height:288px;background:linear-gradient(180deg,#bfe3f7 0%,#e8e2d2 45%,#b9a58a 70%,#8a8f8e 100%)}
.person-photo{position:absolute;right:20px;top:356px;width:240px;height:284px;background:linear-gradient(180deg,#f3ded0 0%,#ffffff 50%,#3d4654 100%);border-radius:120px 120px 0 0}
.speech{position:absolute;left:510px;top:392px;width:126px;height:126px;border-radius:50%;background:var(--white);border:3px solid var(--blue);display:flex;align-items:center;justify-content:center;text-align:center;font-family:"M PLUS Rounded 1c",sans-serif;font-weight:900;font-size:24px;line-height:1.25;color:var(--blue);transform:rotate(-12deg);white-space:nowrap}

.compare{position:absolute;left:0;top:648px;width:846px;height:215px;display:flex;gap:6px}
.compare-wall{flex:0 0 210px;background:linear-gradient(135deg,#9a9d97,#c5c6be 50%,#7d827c)}
.compare-before{flex:1;position:relative;background:linear-gradient(160deg,#4f524d,#6f706a 60%,#3e403c)}
.compare-after{flex:1;position:relative;background:linear-gradient(160deg,#c9c8c1,#e6e5df 60%,#b7b6ae)}
.compare-tile{flex:0 0 180px;background:linear-gradient(135deg,#c9a486,#e0c2a6 50%,#b98c6b)}
.label{position:absolute;bottom:10px;padding:3px 18px;font-weight:700;font-size:22px;border-radius:4px}
.compare-before .label{right:10px;background:#2d2f2e;color:var(--white)}
.compare-after .label{left:10px;background:var(--blue);color:var(--white)}
.arrow{position:absolute;left:405px;top:732px}

.lower{position:absolute;left:0;top:868px;width:846px;height:332px;background:linear-gradient(180deg,#ffffff 0%,#e8f7fd 100%)}
.explain-bubble{position:absolute;left:12px;top:884px;width:212px;height:118px;background:var(--yellow);border:3px solid var(--navy);border-radius:10px;display:flex;align-items:center;justify-content:center;text-align:center;font-family:"M PLUS Rounded 1c",sans-serif;font-weight:900;font-size:20px;line-height:1.4;color:var(--navy);white-space:nowrap}
.staff-photo{position:absolute;left:22px;top:1010px;width:190px;height:166px;background:linear-gradient(180deg,#f2dccb 0%,#ffffff 45%,#2f88c9 100%);border-radius:95px 95px 0 0}
.water-note{position:absolute;left:10px;top:1178px;font-size:13px;color:var(--ink);white-space:nowrap}

.worktime{position:absolute;left:310px;top:884px;background:var(--blue);color:var(--white);font-family:"M PLUS Rounded 1c",sans-serif;font-weight:900;font-size:30px;padding:4px 22px;border-radius:24px;white-space:nowrap}
.range-note{position:absolute;left:618px;top:894px;font-size:16px;font-weight:500;white-space:nowrap}
.price{position:absolute;left:300px;top:920px;font-family:"M PLUS Rounded 1c",sans-serif;font-weight:900;color:var(--blue);font-size:98px;line-height:1;letter-spacing:-2px;-webkit-text-stroke:3px var(--white);paint-order:stroke fill;text-shadow:0 4px 0 var(--navy);white-space:nowrap}
.price .tax{font-size:26px;letter-spacing:0;vertical-align:18px}
.price .yen{font-size:62px}

.company-mark{position:absolute;left:232px;top:1060px;width:170px;height:120px;display:flex;flex-direction:column;align-items:center;justify-content:center;gap:8px}
.company-mark .square{width:52px;height:52px;background:var(--turquoise)}
.company-mark span{font-weight:700;font-size:15px;color:var(--blue-dark);white-space:nowrap}

.contact{position:absolute;left:400px;top:1040px;width:430px}
.contact .consult{font-family:"M PLUS Rounded 1c",sans-serif;font-weight:900;font-size:27px;color:var(--navy);white-space:nowrap}
.contact .company{font-weight:700;font-size:20px;margin-top:2px;white-space:nowrap}
.estimate{position:absolute;right:16px;top:1078px;background:var(--blue);color:var(--white);font-weight:700;font-size:18px;padding:4px 16px;border-radius:6px;white-space:nowrap}
.phone-row{display:flex;align-items:center;gap:8px;margin-top:6px}
.phone-row strong{font-family:"M PLUS Rounded 1c",sans-serif;font-weight:900;font-size:46px;color:var(--blue);letter-spacing:1px;white-space:nowrap}
.phone-icon{width:42px;height:42px;border-radius:50%;background:var(--blue);display:flex;align-items:center;justify-content:center}
.staff-line{font-size:13.5px;margin-top:2px;white-space:nowrap}
</style>
</head>
<body>
<main class="flyer">
  <div class="hero-bg">
    <svg class="rays" width="846" height="400" viewBox="0 0 846 400" aria-hidden="true">
      <g fill="#ffffff" opacity="0.55">
        <polygon points="423,160 0,0 120,0"/>
        <polygon points="423,160 260,0 360,0"/>
        <polygon points="423,160 490,0 590,0"/>
        <polygon points="423,160 720,0 846,0"/>
        <polygon points="423,160 846,140 846,240"/>
        <polygon points="423,160 0,150 0,250"/>
      </g>
    </svg>
  </div>

  <div class="tagline">数年来の汚れが<em>一気に</em>落ちる!</div>

  <aside class="weekday-badge">
    <div class="badge-title">平日割引</div>
    <p>火曜日・水曜日は<br>特別料金にて実施</p>
    <small>空き状況はお電話に<br>てご確認下さい</small>
  </aside>

  <h1 class="main-title">外構洗浄</h1>

  <div class="house-photo" role="img" aria-label="外構のある戸建て住宅の街並み写真"></div>
  <div class="person-photo" role="img" aria-label="エプロン姿で笑顔の女性の写真"></div>
  <div class="speech">プロって<br>すごい!</div>

  <p class="lead">プロが業務用の高圧洗浄機を使い、ご自宅の外構・駐車場(ガレージ)・ブロック塀・玄関タイル・をキレイにします!</p>

  <section class="compare">
    <div class="compare-wall" role="img" aria-label="高圧洗浄中のブロック塀の写真"></div>
    <div class="compare-before" role="img" aria-label="洗浄前の汚れた床面の写真"><span class="label">Before</span></div>
    <div class="compare-after" role="img" aria-label="洗浄後のきれいな床面の写真"><span class="label">After</span></div>
    <div class="compare-tile" role="img" aria-label="きれいになった玄関タイルの写真"></div>
  </section>
  <svg class="arrow" width="40" height="50" viewBox="0 0 40 50" aria-hidden="true"><polygon points="4,5 36,25 4,45" fill="#fff04a" stroke="#13306e" stroke-width="3"/></svg>

  <div class="lower"></div>
  <div class="explain-bubble">施工料金等、丁寧に<br>分かりやすく<br>ご説明します。</div>
  <div class="staff-photo" role="img" aria-label="作業着姿の男性スタッフの写真"></div>
  <p class="water-note">※作業時は水道をお借りします</p>

  <div class="worktime">作業時間2-3時間</div>
  <p class="range-note">※範囲によって異なります</p>
  <p class="price">33,000<span class="tax">(税込)</span><span class="yen">円~</span></p>

  <div class="company-mark"><div class="square"></div><span>ミドリノハウジング</span></div>

  <section class="contact">
    <p class="consult">まずは、お気軽にご相談下さい。</p>
    <p class="company">株式会社ミドリノハウジング</p>
    <div class="phone-row">
      <span class="phone-icon"><svg width="24" height="24" viewBox="0 0 24 24" aria-hidden="true"><path fill="#fff" d="M6.6 10.8c1.4 2.8 3.8 5.1 6.6 6.6l2.2-2.2c.3-.3.7-.4 1-.2 1.1.4 2.300.6 3.6.6.6 0 1 .4 1 1V20c0 .6-.4 1-1 1C10.6 21 3 13.4 3 4c0-.6.4-1 1-1h3.5c.6 0 1 .4 1 1 0 1.3.2 2.5.6 3.6.1.3 0 .7-.2 1z"/></svg></span>
      <strong>094-318-5562</strong>
    </div>
    <p class="staff-line">担当:坂巻(さかまき)・梅沢(うめざわ) 営業時間:9:00~19:00</p>
  </section>
  <div class="estimate">お見積り無料</div>
</main>
</body>
</html>
```